Tarvo Methode
Ich benötige ein E-Book Cover im jpg-Format. Das Vorschaubild sollte im E-Book-Shop (z.B. Verbano Lesa) gut lesbar sein. Das Seiten Verhältnis (Höhe/Breite) sollte 1,6 sein und die Breite mindestens 1400 Pixel betragen. Der Titel der Buchserie heißt "Tarvo Methode". "Mirolat-9" ist ein Untertitel der über die Spielsystem Varianten informiert.Auf meinem Cover müssen noch folgende Sätze platziert werden: "Der Spieler muss keine Zahlen auswählen !" und "105 Mustertabellen mit Tippreihen". Als Beispiel zur Plazierung dieser Sätze schicke ich Ihnen meinen Entwurf vom E-Book Cover als Anhang zu.

```html
<!DOCTYPE html>
<html lang="de">
<head>
<meta charset="utf-8">
<title>Tarvo Methode – Mirolat-9</title>
<link rel="stylesheet" href="https://fonts.googleapis.com/css2?family=Oswald:wght@700&family=Open+Sans:ital,wght@0,600;1,600;1,700&display=swap">
<style>
  :root {
    --stage: #1c1c1c;
    --green: #22a035;
    --dark: #262629;
    --white: #ffffff;
    --ink: #2a2a2c;
    --photo-light: #f4f4f4;
    --photo-mid: #d6d6d6;
    --photo-shade: #c9c9c9;
  }
  * { margin: 0; padding: 0; box-sizing: border-box; }
  html, body {
    width: 1140px; height: 1200px; overflow: hidden;
    background: var(--stage);
  }
  .cover {
    position: absolute; left: 280px; top: 135px;
    width: 580px; height: 928px;
    background: var(--photo-light);
    overflow: hidden;
    box-shadow: 0 4px 14px rgba(0,0,0,.6);
  }
  .cover-photo {
    position: absolute; left: 0; top: 214px; width: 580px; height: 714px;
    background: linear-gradient(180deg,
      var(--photo-mid) 0%,
      #e6e6e6 30%,
      var(--photo-shade) 55%,
      #e4e4e4 72%,
      var(--photo-light) 100%);
  }
  .series-header {
    position: absolute; left: 0; top: 0; width: 580px; height: 205px;
    background: var(--green);
  }
  .header-rule {
    position: absolute; left: 0; top: 205px; width: 580px; height: 9px;
    background: var(--white);
  }
  .series-tag {
    position: absolute; left: 36px; top: 0; width: 243px; height: 80px;
    background: var(--dark);
  }
  .series-tag .bookmark { position: absolute; left: 19px; top: 0; }
  .series-tag .label {
    position: absolute; left: 46px; top: 33px;
    font: 600 32px/1 "Open Sans", sans-serif; color: var(--white);
  }
  .series-title {
    position: absolute; left: 0; top: 108px; width: 580px;
    text-align: center;
    font: 700 76px/1 "Oswald", sans-serif; color: var(--white);
    letter-spacing: 0.5px;
  }
  .subtitle-band {
    position: absolute; left: 227px; top: 217px; width: 353px; height: 91px;
    background: var(--dark);
    clip-path: polygon(27px 0, 100% 0, 100% 100%, 0 100%);
  }
  .subtitle-band span {
    position: absolute; right: 36px; top: 18px;
    font: italic 600 46px/1.1 "Open Sans", sans-serif; color: var(--white);
  }
  .feature-box { position: absolute; left: 0; top: 317px; }
  .feature-list {
    position: absolute; left: 36px; top: 337px; list-style: none;
    font: italic 700 33px/1.17 "Open Sans", sans-serif; color: var(--ink);
  }
  .feature-list li { position: relative; padding-left: 24px; margin-bottom: 8px; }
  .feature-list li::before {
    content: ""; position: absolute; left: 0; top: 13px;
    width: 15px; height: 15px; border-radius: 50%; background: var(--green);
  }
  .author-band {
    position: absolute; left: 0; top: 858px; width: 402px; height: 70px;
    background: var(--dark);
    clip-path: polygon(0 0, 100% 0, 384px 100%, 0 100%);
  }
  .author-band span {
    position: absolute; left: 36px; top: 15px;
    font: italic 600 33px/1.2 "Open Sans", sans-serif; color: var(--white);
  }
  .footer-rule {
    position: absolute; left: 380px; top: 889px; width: 200px; height: 8px;
    background: var(--white);
  }
  .footer-band {
    position: absolute; left: 380px; top: 897px; width: 200px; height: 31px;
    background: var(--green);
  }
</style>
</head>
<body>
  <div class="cover">
    <div class="cover-photo" role="img" aria-label="Foto: Reihen weißer Kugeln hinter einer einzelnen grünen Kugel auf hellem Grund"></div>

    <div class="series-header"></div>
    <div class="header-rule"></div>

    <div class="series-tag">
      <svg class="bookmark" width="13" height="66" viewBox="0 0 13 66" aria-hidden="true">
        <polygon points="0,0 13,0 13,66 6.5,58 0,66" fill="#ffffff"/>
      </svg>
      <span class="label">Buch-Reihe</span>
    </div>

    <h1 class="series-title">TARVO-METHODE</h1>

    <div class="subtitle-band"><span>Mirolat-9</span></div>

    <svg class="feature-box" width="470" height="220" viewBox="0 0 470 220" aria-hidden="true">
      <polygon points="0,1 467,1 409,218 0,218" fill="rgba(255,255,255,0.45)" stroke="#2a2a2c" stroke-width="2"/>
    </svg>
    <ul class="feature-list">
      <li>Der Spieler muss keine<br>Zahlen auswählen!</li>
      <li>105 Mustertabellen<br>mit Tippreihen</li>
    </ul>

    <div class="footer-rule"></div>
    <div class="footer-band"></div>
    <div class="author-band"><span>Bertold Uxanski</span></div>
  </div>
</body>
</html>
```